Medical Internet Marketing Company Needs a Site!

We need a new, fresh website for our search engine optimization and social media marketing company. We specialize in helping medical practices, doctors, physicians, and hospitals with their online presence and web ranking. The site should lean towards being suited for these audiences.

We have several examples of website that we like as well as things that we like about them.

Here are sites that we enjoy.

www.brightwavepromo.com

It's a good design for the site all around. The videos, buttons, and images are all excellent. They did a fine job.

- We really like their "contact us" side bar and want to include one like it on the secondary pages.

www.kestrelgrow.net

- We don't like the "thickness" of the top navigation bar.
- We like the page colors, easy navigation, and big call to action phone number in the top right corner.

http://www.tulavo.com/

Out of all the examples provided, Tulavo is our favorite and closest look and style to what we are looking for.

- We really like the openness of the design, such as space between the text and background.

- We want a price page in a style very similar to their pricing page with the services listed and check-marks, etc. although we intend to have multiple service package columns much like Kestrel's SEO pricing page.

- The way the video fits into the home page header is very organized, simple, and attention grabbing. We intend to place a slider with videos here.

- We need a page design that will allow for an image slider like Tulavo's Features page.

Here's a great example of a medical internet marketing website: http://www.dorvanta.com/

Target Market(s)

Our target market is doctors, typically male and typically 40-45 years old. I

Industry/Entity Type

Marketing

Requirements
Must have
• The homepage should have a slider in the video. Interior pages should have a video in the very top similar to how they do it on www.brightwavepromo.com

The top navigation tabs needed are:
- Home
- Solutions
- Resources
- About
- Why Zentrol
- Contact

The sidebar should have a GREAT call to action in it on interior pages.

There should be one interior page that is similar to this - http://www.tulavo.com/pricing/

There needs to be a page with multiple boxes that take up a row of the web page's body. This page will house all the case studies similar to brightwave promo's: http://www.brightwavepromo.com/success-stories/case-studies/ The one exception is we want the case studies to be inside of "boxes" instead of between horizontal lines like brightwave promo's.
Nice to have
• Color, professional, and clean. GREAT use of calls to actions.

```html
<!DOCTYPE html>
<html lang="en">
<head>
<meta charset="utf-8">
<title>Zentrol – Page Heading</title>
<link href="https://fonts.googleapis.com/css2?family=Cabin:wght@400;500&family=Carlito:wght@400;700&family=Ubuntu:wght@500;700&display=swap" rel="stylesheet">
<style>
:root{
  --blue:#3d9ad1;
  --sea:#3b9ace;
  --sea-dark:#2e7fac;
  --green:#8cc63f;
  --grey-text:#444;
  --nav-text:#555;
  --logo-grey:#a3a3a3;
  --panel:#ffffff;
  --form-bg:#d6eaf4;
  --form-head:#1f6a8e;
  --orange-a:#ffc21a;
  --orange-b:#ff8a00;
  --footer:#555555;
  --footer-link:#4fb3ea;
  --footer-text:#e8e8e8;
  --rule:#dcdcdc;
}
*{box-sizing:border-box;margin:0;padding:0}
html,body{width:1026px;height:1200px;overflow:hidden}
body{position:relative;background:#f4f4f4;font-family:"Carlito",Calibri,sans-serif;color:var(--grey-text)}
.sky{position:absolute;left:0;top:0;width:1026px;height:400px;background:linear-gradient(#fbfbfb,#efefef)}
.sea{position:absolute;left:0;top:400px;width:1026px;height:686px;background:linear-gradient(var(--sea) 0,var(--sea) 88%,var(--sea-dark) 100%)}
.footer{position:absolute;left:0;top:1086px;width:1026px;height:114px;background:var(--footer);border-top:1px solid #777}

.brand{position:absolute;left:99px;top:27px;display:flex;align-items:center;gap:10px}
.brand-mark{width:32px;height:32px;background:var(--logo-grey)}
.brand-name{font-family:"Cabin",sans-serif;font-size:42px;font-weight:400;color:var(--logo-grey);letter-spacing:3px;line-height:1}
.call{position:absolute;right:105px;top:28px;font-family:"Cabin",sans-serif;font-size:26px;color:var(--blue)}
.call span{color:var(--green)}

.nav{position:absolute;left:98px;top:84px;width:827px;border-top:1px solid var(--rule)}
.nav-marker{position:absolute;left:30px;top:-2px;width:0;height:0;border-left:13px solid transparent;border-right:13px solid transparent;border-top:10px solid #f7b233}
.nav a{position:absolute;top:17px;font-family:"Cabin",sans-serif;font-size:17px;color:var(--nav-text);text-decoration:none;white-space:nowrap}

.main{position:absolute;left:98px;top:139px;width:827px;height:905px;background:var(--panel)}
.page-title{position:absolute;left:30px;top:24px;font-family:"Cabin",sans-serif;font-weight:400;font-size:36px;color:var(--blue)}
.page-sub{position:absolute;left:32px;top:81px;font-family:"Cabin",sans-serif;font-weight:400;font-size:20px;color:var(--green)}
.copy{position:absolute;left:32px;top:120px;width:462px;font-size:13.4px;line-height:18.8px;text-align:justify}
.copy p{margin-bottom:18.8px}
.divider{position:absolute;left:527px;top:30px;width:3px;height:861px;background:#e2e2e2}

.consult{position:absolute;left:559px;top:30px;width:240px;height:263px;background:var(--form-bg);padding:13px 24px 0 24px}
.consult h2{font-family:"Cabin",sans-serif;font-weight:400;font-size:14.5px;color:var(--form-head);margin-bottom:10px;margin-left:-1px}
.field{display:block;font-size:11.5px;color:#333;margin-bottom:9px}
.field input{display:block;width:192px;height:21px;border:1px solid #c5d7e0;background:#fff;margin-top:2px}
.form-foot{display:flex;justify-content:space-between;align-items:center;width:192px;font-size:11.5px;color:#333;margin-top:-2px}
.submit{width:76px;height:24px;border:1px solid #e07a10;border-radius:5px;background:linear-gradient(#ffb54a,#f7870f);color:#fff;font-family:"Carlito",sans-serif;font-weight:700;font-size:13px}

.whitepaper{position:absolute;left:559px;top:322px;width:240px;height:208px;background:linear-gradient(135deg,var(--orange-a),#ffb000 55%,var(--orange-b));padding:22px 0 0 25px;font-family:"Ubuntu",sans-serif;color:#fff;text-shadow:0 1px 1px rgba(150,80,0,.35)}
.whitepaper .big{font-size:31px;font-weight:700;line-height:32px}
.whitepaper .small{font-size:21.5px;font-weight:700;line-height:25.5px;margin-top:2px}
.download{position:absolute;left:25px;top:139px;width:188px;height:41px;border:1px solid #999;border-radius:4px;background:linear-gradient(#fafafa,#cfcfcf);color:#111;font-family:"Ubuntu",sans-serif;font-weight:700;font-size:20px;text-shadow:none}

.foot-links{position:absolute;top:1106px;list-style:none;font-size:11.5px;line-height:20.6px}
.foot-links a{color:var(--footer-link);text-decoration:none}
.foot-rule{position:absolute;top:1095px;width:1px;height:95px;background:#8a8a8a}
.address{position:absolute;left:417px;top:1106px;font-size:11.5px;line-height:15.4px;color:var(--footer-text);font-style:normal}
.copyright{position:absolute;right:99px;top:1103px;font-family:"Cabin",sans-serif;font-size:11.5px;color:var(--footer-text)}
.social{position:absolute;left:771px;top:1127px;display:flex;gap:14px}
.social span{width:28px;height:28px;border-radius:50%;background:#cfcfcf}
</style>
</head>
<body>
<div class="sky"></div>
<div class="sea"></div>

<header>
  <div class="brand"><span class="brand-mark"></span><span class="brand-name">ZENTROL</span></div>
  <div class="call"><span>Call</span> 0198 765 432</div>
  <nav class="nav">
    <span class="nav-marker"></span>
    <a href="#" style="left:21px">HOME</a>
    <a href="#" style="left:131px">SOLUTIONS</a>
    <a href="#" style="left:286px">RESOURCES</a>
    <a href="#" style="left:439px">ABOUT</a>
    <a href="#" style="left:558px">WHY ZENTROL</a>
    <a href="#" style="left:720px">CONTACT</a>
  </nav>
</header>

<main class="main">
  <h1 class="page-title">PAGE HEADING</h1>
  <h2 class="page-sub">SOLLICITUDIN GRAVIDA MI SED PORTTITOR</h2>
  <div class="copy">
    <p>Maecenas accumsan ligula arcu, a sollicitudin tortor. Quisque et lacus libero. Nullam lacinia, lorem vitae faucibus commodo, dui magna pellentesque lorem, congue aliquam elit leo nec justo. Proin auctor, nibh ut iaculis ornare, sem mauris congue tortor, eget tristique nibh dui eget nisi. Donec ultricies quam vitae nisl eleifend condimentum. Vivamus odio orci, interdum imperdiet dictum ac, tempor eget libero. Pellentesque non sapien erat. Donec a est tortor, sit amet ultricies nulla. Mauris quis rhoncus velit. Cras sit amet eros massa, eget volutpat quam. Cras bibendum fringilla pulvinar. Donec tempor aliquet tincidunt. Maecenas sapien augue, pellentesque id interdum a, venenatis vel tellus.</p>
    <p>Sed vel ipsum mi, et vestibulum diam. Pellentesque ut dui in sem varius viverra. Vivamus tempor mi a risus congue eleifend. Mauris eu augue in orci dapibus hendrerit. Nullam eu odio eget dolor egestas facilisis vel eu erat. Suspendisse tincidunt suscipit libero, nec tincidunt quam tempus in. Maecenas consectetur arcu bibendum nibh eleifend malesuada. Quisque id eros nunc.</p>
    <p>Curabitur luctus pulvinar facilisis. Phasellus varius sagittis sagittis. Fusce felis lacus, luctus a feugiat vitae, ultrices rhoncus eros. Mauris augue nisi, hendrerit nec pulvinar eget, viverra eu ipsum. In hac habitasse platea dictumst. Maecenas ornare, diam ac gravida porta, risus lorem feugiat enim, eu fermentum dui turpis quis urna. Cras egestas accumsan mauris in tempor. Maecenas tincidunt, enim tincidunt blandit mattis, leo diam hendrerit ipsum, ac gravida nisi urna eget urna.</p>
    <p>Aliquam in nisl augue, et tincidunt justo. Nulla sed velit odio. Nullam facilisis magna vitae velit pellentesque mollis. Nulla neque nisl, ornare vel dapibus vitae, adipiscing ac nunc. Nulla facilisi. Curabitur laoreet mollis sollicitudin. Proin dignissim tempus tortor a dignissim. Donec et orci consectetur ligula dictum tristique. Praesent metus dui, vulputate quis imperdiet eu, aliquet quis lorem. Mauris id felis vitae velit varius vehicula ac nec lacus.</p>
    <p>Mauris augue nisi, hendrerit nec pulvinar eget, viverra eu ipsum. In hac habitasse platea dictumst. Maecenas ornare, diam ac gravida porta, risus lorem feugiat enim, eu fermentum dui turpis quis urna. Cras egestas accumsan mauris in tempor. Maecenas tincidunt, enim tincidunt blandit mattis, leo diam hendrerit ipsum, ac gravida nisi urna eget urna.</p>
  </div>
  <div class="divider"></div>

  <aside>
    <form class="consult">
      <h2>GET A FREE CONSULTATION</h2>
      <label class="field">Domain (URL)*<input type="text"></label>
      <label class="field">Name*<input type="text"></label>
      <label class="field">Phone*<input type="text"></label>
      <label class="field">Email*<input type="text"></label>
      <div class="form-foot"><span>*Required</span><button class="submit" type="button">Submit</button></div>
    </form>
    <div class="whitepaper">
      <div class="big">DOWNLOAD</div>
      <div class="small">OUR FREE WHITE<br>PAPER ABOUT<br>MEDICAL SEO</div>
      <button class="download" type="button">Download Now</button>
    </div>
  </aside>
</main>

<footer class="footer"></footer>
<ul class="foot-links" style="left:99px">
  <li><a href="#">Why Zentrol</a></li>
  <li><a href="#">pricing</a></li>
  <li><a href="#">Solutions</a></li>
  <li><a href="#">Features</a></li>
</ul>
<ul class="foot-links" style="left:220px">
  <li><a href="#">Resources</a></li>
  <li><a href="#">Case Study</a></li>
  <li><a href="#">About us</a></li>
</ul>
<div class="foot-rule" style="left:347px"></div>
<address class="address">ZENTROL<br>Unit 12, Lakeside Court<br>88 Marlow Street, Hobart,<br>Tasmania<br>Phone: 0198 765 432</address>
<div class="foot-rule" style="left:639px"></div>
<div class="copyright">Copyright © 2012 ZENTROL. All right reserved.</div>
<div class="social"><span></span><span></span><span></span><span></span></div>
</body>
</html>
```